Legal Consultant: Book cover for "Silver Ridge Transitions" in Australia.

This project is for the desiign of the front cover of a book t be published in perfect bond (A5) and as an eBook.

The target readers are Australian law firm partners.

I am a lawyer and senior legal recruitment consultant specialisng in the recruitment of law firm partners. I have written a short book that advises law firm partners how to make a lateral move to another law firm. It's simply about recruitment at a senior level. The book sets out the steps to maximise the partner's opportunity to engage the services of a senior legal recruitment consultant and then identify suitable law firms, interview techniques and preparation. A key element in the book is the preparation of various documents to submit to potential law firms eg CV, business plan, financial performance.

I know the eBook design has to 'grab" the reader so the title will need to jump out at the reader.

Target Market(s)

Senior law firm partners in Australia

Industry/Entity Type

Graphic Design

Requirements
Must have
• The cover must also be suitable for eBook publication. Therefore it must stand out from competitive publications.
Nice to have
• A design suitable for senior professional services executves.
Should not have
• No cliches eg shaking hands, two men in suits, judge's gavel etc

```html
<!DOCTYPE html>
<html lang="en">
<head>
<meta charset="utf-8">
<title>A Partner's Guide: Planning Your Next Chapter</title>
<link rel="stylesheet" href="https://fonts.googleapis.com/css2?family=Open+Sans:ital,wght@0,700;1,400&family=Saira+Condensed:wght@700&display=swap">
<style>
  :root {
    --navy-top: #2a2f9e;
    --navy-deep: #1c1f86;
    --navy-low: #15186e;
    --sky-high: #4a5cb8;
    --sky-dusk: #b9a9d6;
    --skyline: #1a1a33;
    --water: #8f93cf;
    --orange: #f7a21b;
    --orange-dark: #d9820a;
    --white: #ffffff;
  }
  * { margin: 0; padding: 0; box-sizing: border-box; }
  html, body {
    width: 846px; height: 1200px; overflow: hidden;
    background: var(--navy-deep);
  }
  .cover {
    position: relative; width: 846px; height: 1200px; overflow: hidden;
    background: linear-gradient(180deg, var(--navy-top) 0%, var(--navy-deep) 55%, var(--navy-low) 100%);
  }
  .cover-photo {
    position: absolute; left: 0; top: 120px; width: 846px; height: 560px;
    background: linear-gradient(180deg,
      var(--sky-high) 0%, #7d84c8 22%, var(--sky-dusk) 36%,
      #6b6a98 42%, var(--skyline) 46%, #3b3f7a 52%,
      var(--water) 62%, #6f74c0 80%, var(--navy-deep) 100%);
  }
  .cover-photo::after {
    content: ""; position: absolute; inset: 0;
    background: linear-gradient(180deg, rgba(28,31,134,0) 60%, var(--navy-deep) 100%);
  }
  .series-label, .title {
    position: absolute; left: 0; width: 846px; display: block;
  }
  .series-label { top: 14px; height: 100px; }
  .series-label text {
    font-family: "Open Sans", sans-serif; font-weight: 700;
    font-size: 72px; fill: var(--orange);
  }
  .title { top: 590px; height: 300px; }
  .title text {
    font-family: "Saira Condensed", sans-serif; font-weight: 700;
    font-size: 145px; fill: var(--white);
  }
  .author {
    position: absolute; left: 0; width: 846px; top: 968px; text-align: center;
    font-family: "Open Sans", sans-serif; font-weight: 700;
    font-size: 82px; line-height: 1; color: var(--orange);
  }
  .credentials {
    position: absolute; left: 0; width: 846px; top: 1086px; text-align: center;
    font-family: "Open Sans", sans-serif; font-style: italic; font-weight: 400;
    font-size: 48px; line-height: 1; color: var(--white);
  }
  .footer-bar {
    position: absolute; left: 0; bottom: 0; width: 846px; height: 36px;
    background: linear-gradient(180deg, var(--orange) 0%, var(--orange-dark) 100%);
  }
</style>
</head>
<body>
  <main class="cover">
    <div class="cover-photo" role="img" aria-label="Photograph of a city skyline at dusk across calm harbour water"></div>

    <svg class="series-label" viewBox="0 0 846 100" aria-label="A Partner's Guide:">
      <text x="423" y="78" text-anchor="middle" textLength="740" lengthAdjust="spacingAndGlyphs">A PARTNER’S GUIDE:</text>
    </svg>

    <svg class="title" viewBox="0 0 846 300" aria-label="Planning Your Next Chapter">
      <text x="423" y="144" text-anchor="middle" textLength="744" lengthAdjust="spacingAndGlyphs">PLANNING YOUR</text>
      <text x="423" y="274" text-anchor="middle" textLength="744" lengthAdjust="spacingAndGlyphs">NEXT CHAPTER</text>
    </svg>

    <p class="author">Daniel Marsh</p>
    <p class="credentials">LL.B Barrister-at-Law</p>

    <div class="footer-bar"></div>
  </main>
</body>
</html>
```